Seeking Talented PSD Designer for Real Estate Finance Web Site

Hello ...
Need a minimalist design for a high - end finance web site that conveys prestige / sophistication / class ... Below are comps for this project ...
http://www.copperlanefunding.com/
http://mirowayfunding.com/
http://www.tolvinedgp.com/
http://quillanfunding.com/
Look forward too receiving proposals for this project ....
Target Market(s)
Commerciale entities seeking more than $500.0 k in interim capital ... These could include apartment owners / construction managers / restaurant owners / hotels / golf courses ...
Industry/Entity Type
Real Estate
Number of Pages Required
1 page
Requirements
Must have
- Super high quality graphic design ... Has to be marketable and convert customers to contact us ...
- Please refer to logo concept four ....
Should not have
- clunky / poor fonts /

```html
<!DOCTYPE html>
<html lang="en">
<head>
<meta charset="utf-8">
<title>Halvorn Capital</title>
<link href="https://fonts.googleapis.com/css2?family=Lato:wght@400;700&family=Oswald:wght@300;400&display=swap" rel="stylesheet">
<style>
:root{
  --brand-blue:#2f76b7;
  --ink:#3d3d3d;
  --ink-soft:#555;
  --tile-bg:#f2f2f2;
  --tile-edge:#dcdcdc;
  --icon-grey:#6b6b6b;
  --white:#fff;
  --footer-text:#f1f5fa;
}
*{margin:0;padding:0;box-sizing:border-box}
html,body{width:1200px;height:796px;overflow:hidden}
body{font-family:"Lato",sans-serif;color:var(--ink);position:relative;background:#e9e9ea}
.hero-photo{position:absolute;left:0;top:0;width:1200px;height:727px;
  background:
    radial-gradient(ellipse 380px 260px at 1000px 260px,rgba(190,160,140,.55),transparent 70%),
    radial-gradient(ellipse 360px 300px at 180px 200px,rgba(210,180,170,.5),transparent 70%),
    radial-gradient(ellipse 420px 120px at 900px 470px,rgba(70,120,190,.35),transparent 70%),
    linear-gradient(180deg,#b9b9bc 0%,#d6d6d8 40%,#e7e8ea 70%,#d9dadd 100%);}
.sidebar{position:absolute;left:131px;top:0;width:225px;height:459px;
  background:rgba(255,255,255,.78);border-radius:0 0 112px 112px;}
.brand{position:absolute;left:0;top:8px;width:225px;text-align:center}
.brand-mark{display:block;margin:0 auto;width:74px;height:74px;border-radius:50%;background:#3f5373}
.brand-name{display:block;margin-top:16px;font-family:"Lato",sans-serif;font-weight:400;font-size:27px;letter-spacing:5px;color:#4a5a72}
.nav{position:absolute;left:0;top:188px;width:225px;list-style:none;text-align:center}
.nav li{height:37.5px;line-height:37.5px;font-weight:700;font-size:15.5px;color:var(--ink);
  background:linear-gradient(90deg,transparent,rgba(120,120,120,.5),transparent) bottom/150px 1px no-repeat}
.nav li:last-child{background:none}
.nav li.active{color:var(--brand-blue)}
.topbar{position:absolute;top:0;right:129px;display:flex;align-items:flex-start;gap:16px}
.phone{display:flex;align-items:center;gap:8px;margin-top:4px;color:var(--white);font-weight:700;font-size:20px}
.login{display:flex;align-items:center;gap:6px;height:32px;padding:0 12px 0 8px;background:rgba(235,235,235,.92);
  border-radius:0 0 4px 4px;color:#2c5590;font-weight:700;font-size:18px}
.headline{position:absolute;left:424px;top:218px;width:600px;text-align:center;font-family:"Oswald",sans-serif;font-weight:300;
  font-size:42px;line-height:57px;color:var(--white);letter-spacing:.5px;text-shadow:0 1px 4px rgba(0,0,0,.35)}
.services{position:absolute;top:492px;left:132px;display:flex;gap:12.5px}
.tile{position:relative;width:225px;height:195px;background:linear-gradient(180deg,#f7f7f7,#ececec);
  box-shadow:0 8px 6px -4px rgba(0,0,0,.55);text-align:center}
.tile svg.icon{display:block;margin:29px auto 0}
.tile-label{margin-top:12px;font-weight:700;font-size:18.5px;line-height:23px;color:#3a3a3a}
.tile.active .tile-label{color:var(--brand-blue)}
.corner{position:absolute;right:0;bottom:0;width:26px;height:26px}
.footer{position:absolute;left:0;top:727px;width:1200px;height:69px;background:var(--brand-blue)}
.copyright{position:absolute;left:135px;top:26px;font-size:15px;color:var(--footer-text)}
.social{position:absolute;right:59px;top:20px;display:flex;gap:5px}
.social span{width:29px;height:29px;border-radius:50%;border:1.5px solid rgba(255,255,255,.55)}
</style>
</head>
<body>
<div class="hero-photo" role="img" aria-label="Photo of business people reviewing financial charts with a pen at a desk"></div>

<aside class="sidebar">
  <div class="brand"><span class="brand-mark"></span><span class="brand-name">HALVORN</span></div>
  <ul class="nav">
    <li class="active">HOME</li>
    <li>ABOUT ME</li>
    <li>INVESTMENT STRATEGY</li>
    <li>NEWS &amp; EVENTS</li>
    <li>OUR TEAM</li>
    <li>CONTACT US</li>
  </ul>
</aside>

<div class="topbar">
  <div class="phone">
    <svg width="27" height="27" viewBox="0 0 27 27"><circle cx="13.5" cy="13.5" r="12.5" fill="none" stroke="#fff" stroke-width="1.6"/><path d="M9 7c1-1 2 0 3 2s0 2-1 3c1 2 2 3 4 4 1-1 1-2 3-1s3 2 2 3c-2 3-6 1-8-1s-5-6-3-10z" fill="#fff"/></svg>
    012-555-0147
  </div>
  <div class="login">
    <svg width="18" height="22" viewBox="0 0 18 22"><path d="M4 10V7a5 5 0 0 1 10 0v3" fill="none" stroke="#333" stroke-width="2.4"/><rect x="2" y="10" width="14" height="11" rx="1.5" fill="#333"/></svg>
    LOGIN
  </div>
</div>

<h1 class="headline">SPECIALIZING IN DIRECT LENDING<br>AND VALUE ORIENTED ACQUISITIONS</h1>

<section class="services">
  <div class="tile active">
    <svg class="icon" width="92" height="92" viewBox="0 0 92 92"><circle cx="46" cy="46" r="46" fill="#2f76b7"/><circle cx="40" cy="34" r="11" fill="#fff"/><path d="M22 64c0-12 8-18 18-18s14 4 16 8v10z" fill="#fff"/><circle cx="59" cy="57" r="14" fill="#fff"/><circle cx="59" cy="57" r="11" fill="#2f76b7"/><path d="M59 50v7l5 4" stroke="#fff" stroke-width="2.4" fill="none"/></svg>
    <p class="tile-label">STRATEGIC<br>PLANNING</p>
    <svg class="corner" viewBox="0 0 26 26"><path d="M26 0V26H0z" fill="#2f76b7"/><path d="M18 16v8M14 20h8" stroke="#fff" stroke-width="2"/></svg>
  </div>
  <div class="tile">
    <svg class="icon" width="94" height="94" viewBox="0 0 94 94"><circle cx="47" cy="47" r="45" fill="#fff" stroke="#777" stroke-width="3"/><circle cx="39" cy="28" r="7" fill="#666"/><path d="M30 38h16v32h-6V54h-4v16h-6z" fill="#666"/><circle cx="58" cy="56" r="15" fill="#fff" stroke="#666" stroke-width="3"/><text x="58" y="63" font-family="Lato,sans-serif" font-weight="700" font-size="19" fill="#666" text-anchor="middle">$</text></svg>
    <p class="tile-label">MANAGEMENT<br>SOLUTIONS</p>
    <svg class="corner" viewBox="0 0 26 26"><path d="M26 0V26H0z" fill="#9a9a9a"/><path d="M18 16v8M14 20h8" stroke="#fff" stroke-width="2"/></svg>
  </div>
  <div class="tile">
    <svg class="icon" width="94" height="94" viewBox="0 0 94 94"><circle cx="47" cy="47" r="45" fill="#fff" stroke="#777" stroke-width="3"/><rect x="25" y="27" width="38" height="32" fill="none" stroke="#666" stroke-width="4"/><path d="M30 50l7-9 6 6 7-10 7 6" fill="none" stroke="#666" stroke-width="3"/><circle cx="60" cy="57" r="7" fill="#fff" stroke="#666" stroke-width="3"/><path d="M65 62l7 7" stroke="#666" stroke-width="4"/></svg>
    <p class="tile-label">FINANCIAL<br>ANALYSIS</p>
    <svg class="corner" viewBox="0 0 26 26"><path d="M26 0V26H0z" fill="#9a9a9a"/><path d="M18 16v8M14 20h8" stroke="#fff" stroke-width="2"/></svg>
  </div>
  <div class="tile">
    <svg class="icon" width="94" height="94" viewBox="0 0 94 94"><circle cx="47" cy="47" r="45" fill="#fff" stroke="#777" stroke-width="3"/><rect x="22" y="32" width="48" height="32" fill="#666"/><path d="M22 32l24 18 24-18" fill="none" stroke="#fff" stroke-width="2.5"/><path d="M48 62c2-8 8-11 14-11v-5l10 9-10 9v-5c-6 0-10 1-14 3z" fill="#fff" stroke="#666" stroke-width="2"/></svg>
    <p class="tile-label">QUICK<br>INQUIRY</p>
    <svg class="corner" viewBox="0 0 26 26"><path d="M26 0V26H0z" fill="#9a9a9a"/><path d="M18 16v8M14 20h8" stroke="#fff" stroke-width="2"/></svg>
  </div>
</section>

<footer class="footer">
  <p class="copyright">Copyright 2016 Halvorn Capital.&nbsp; All rights reserved.</p>
  <div class="social" aria-label="Social links"><span></span><span></span><span></span><span></span></div>
</footer>
</body>
</html>
```